Flyer for free seminar invite

We are an accident management company.
Need a flyer to invite smash repairers to a free seminar.
Our website is motovista.com.au.
The flyer will be distributed by hand, email and fax.

The seminar will cover:

3 keys to success in 2015

* How to obtain and retain quality fleet work
* How to quote for profit and make insurers pay more
* How to make money from loan vehicles

Please see attached:

* Current brochure
* Logo, artwork

Target Market(s)

car repairers

Industry/Entity Type

Loan

Font styles to use
Sans Serif

Colors
eb1f27

Requirements
Must have
• 1 page
• logo and contact details
• date and location of event
• benefits of attending event
• large font, suitable for faxing

```html
<!DOCTYPE html>
<html lang="en">
<head>
<meta charset="utf-8">
<title>3 Keys to Success in 2015 – Seminar Invitation</title>
<link rel="stylesheet" href="https://fonts.googleapis.com/css2?family=Open+Sans:wght@400;700;800&family=Playfair+Display:wght@400&display=swap">
<style>
  :root {
    --brand-red: #eb1f27;
    --deep-red: #7a0a10;
    --night: #1a0204;
    --ink-white: #ffffff;
    --soft-white: #f3e6e6;
    --gold: #f2c200;
    --page-bg: #e9e9e9;
    --silver: #b9b9b9;
  }
  * { box-sizing: border-box; margin: 0; padding: 0; }
  html, body { width: 1200px; height: 880px; overflow: hidden; }
  body {
    background: var(--page-bg);
    display: flex; align-items: center; justify-content: center;
    font-family: "Open Sans", Arial, sans-serif;
  }
  .flyer {
    position: relative;
    width: 594px; height: 840px;
    overflow: hidden;
    color: var(--ink-white);
    display: flex; flex-direction: column; align-items: center;
    padding: 14px 40px 36px;
    background:
      radial-gradient(circle at 62% 30%, rgba(255,90,80,.85) 0, rgba(235,31,39,.6) 18%, transparent 45%),
      radial-gradient(circle at 85% 12%, rgba(255,160,140,.35) 0, transparent 22%),
      radial-gradient(circle at 20% 70%, rgba(160,20,30,.55) 0, transparent 35%),
      linear-gradient(180deg, #3a0307 0%, var(--deep-red) 30%, #5a050b 65%, var(--night) 100%);
  }
  .flyer__headline-band {
    position: absolute; top: 0; left: 0; right: 0; height: 120px;
    background: linear-gradient(180deg, rgba(0,0,0,.75), transparent);
  }
  .flyer__invitation {
    position: relative;
    font-weight: 800; font-size: 76px; line-height: 1.2; letter-spacing: 4px;
    color: var(--silver); opacity: .8;
  }
  .ornament {
    margin-top: 10px;
    width: 110px; height: 24px;
    background: linear-gradient(90deg, transparent, var(--gold), transparent);
    opacity: .85; border-radius: 12px;
  }
  .ornament--bottom { width: 140px; height: 12px; margin-top: 8px; }
  .event-title {
    margin-top: 8px;
    font-family: "Playfair Display", Georgia, serif;
    font-weight: 400; font-size: 40px; line-height: 1.08;
    text-align: center; text-transform: uppercase; letter-spacing: 1px;
  }
  .event-date {
    margin-top: 18px;
    font-weight: 700; font-size: 23px; white-space: nowrap;
  }
  .topics { margin-top: 8px; list-style: none; width: 500px; }
  .topics__item {
    margin-top: 8px; padding: 5px 12px;
    border: 1.5px dashed rgba(255,255,255,.7); border-radius: 14px;
    text-align: center; font-weight: 700; font-size: 17px; white-space: nowrap;
  }
  .benefits { margin-top: 20px; width: 510px; font-size: 12.5px; line-height: 1.45; color: var(--soft-white); }
  .benefits__heading { font-weight: 700; font-size: 13px; }
  .benefits__list { list-style: none; counter-reset: b; }
  .benefits__list li { counter-increment: b; }
  .benefits__list li::before { content: counter(b) ". "; }
  .flyer__footer {
    margin-top: auto; width: 510px;
    display: flex; align-items: center; gap: 18px;
  }
  .brand { display: flex; flex-direction: column; }
  .brand__name { font-weight: 700; font-size: 28px; line-height: 1.2; letter-spacing: 1px; color: var(--ink-white); }
  .brand__url { font-size: 10px; color: var(--soft-white); }
  .footer__divider { width: 1px; height: 62px; background: var(--soft-white); }
  .contact { font-size: 15px; line-height: 1.4; }
  .contact__label { display: inline-block; width: 70px; }
</style>
</head>
<body>
  <article class="flyer">
    <div class="flyer__headline-band"></div>
    <div class="flyer__invitation">INVITATION</div>

    <div class="ornament" role="img" aria-label="Gold decorative flourish"></div>
    <h1 class="event-title">3 Keys to<br>Success<br>in 2015</h1>
    <div class="ornament ornament--bottom" role="img" aria-label="Gold decorative divider flourish"></div>

    <p class="event-date">Saturday, 20th February, 2015 Sydney</p>

    <ul class="topics">
      <li class="topics__item">How to obtain and retain quality fleet work</li>
      <li class="topics__item">How to quote for profit and make insurers pay more</li>
      <li class="topics__item">How to make money from loan vehicles</li>
    </ul>

    <div class="benefits">
      <p class="benefits__heading">THE BENEFITS:</p>
      <ol class="benefits__list">
        <li>Get paid what you deserve rather than what an insurance company is willing to offer.</li>
        <li>Repair customer vehicles straight away without waiting for approval.</li>
        <li>No more dealing with insurance company assessors.</li>
        <li>Service uninsured people, or anyone else who does not want to go through their own insurer.</li>
        <li>Get paid for providing courtesy cars to customers.</li>
      </ol>
    </div>

    <footer class="flyer__footer">
      <div class="brand">
        <span class="brand__name">MOTOVISTA</span>
        <span class="brand__url">www.motovista.com.au</span>
      </div>
      <div class="footer__divider"></div>
      <div class="contact">
        <p><span class="contact__label">Phone</span>:02 9000 4821</p>
        <p><span class="contact__label">Email</span>:contact@motovista.com.au</p>
        <p><span class="contact__label">website</span>:www.motovista.com.au</p>
      </div>
    </footer>
  </article>
</body>
</html>
```